Financial Dashboard UI design

We are building a financial dashboard for business management teams, and would like a futuristic and sophisticated design (light and dark themes).

There are a total of 3 screens (attached images: nemo1, nemo2, nemo3).
nemo1 image is comprised of 6 scorecards (attached image: scorecard)
This will also need a design.

So, I'm expecting 4 UI designs in total.

I've added some example UI for inspiration. (sample1 , sample2, sample3, sample4).

Thanks

```html
<!DOCTYPE html>
<html lang="en">
<head>
<meta charset="utf-8">
<title>Ledgerline – 2021 U.S Sales</title>
<link href="https://fonts.googleapis.com/css2?family=Montserrat:wght@400;500;600;700&display=swap" rel="stylesheet">
<style>
  :root{
    --sidebar:#141414;
    --accent-blue:#11639b;
    --brand:#2f7fc4;
    --orange:#e85f24;
    --green-cell:#dcf3dc;
    --green-text:#1f7a1f;
    --red-cell:#e0262a;
    --row-line:#e4e8ec;
    --text-dark:#222;
  }
  *{box-sizing:border-box;margin:0;padding:0}
  html,body{width:811px;height:1200px;overflow:hidden;background:#fff;font-family:"Montserrat",sans-serif}
  .canvas{position:relative;width:811px;height:1200px}

  .screen{position:absolute;left:23px;width:763px;display:flex;box-shadow:0 1px 4px rgba(0,0,0,.35)}
  .screen--light{top:23px;height:581px;--content-bg:#fff;--panel-bg:#f0f5f9;--panel-border:#d5dde4;--panel-text:#111;--rule:#c9d0d6}
  .screen--dark{top:624px;height:536px;--content-bg:var(--accent-blue);--panel-bg:#0b1f33;--panel-border:#0b1f33;--panel-text:#fff;--rule:#8797a8}

  .sidebar{width:117px;flex:none;background:var(--sidebar);color:#fff}
  .brand{height:52px;padding:21px 0 0 20px;display:flex;align-items:flex-start;gap:5px;font-weight:600;font-size:10px;color:var(--brand);letter-spacing:.3px}
  .brand-mark{width:7px;height:7px;background:var(--brand);margin-top:2px;flex:none}
  .menu{list-style:none}
  .menu li{height:18.6px;display:flex;align-items:center;padding-left:20px;font-size:6.4px;letter-spacing:.2px}
  .menu li svg{width:6px;height:6px;margin-right:8px;fill:#fff}
  .menu li.is-active{background:var(--accent-blue)}
  .menu li.is-active span{margin-left:3px}
  .screen--dark .menu li{border-bottom:0.6px solid #2b2b2b}

  .content{flex:1;background:var(--content-bg);padding:8px 8px 0 10px;position:relative}
  .panel{background:var(--panel-bg);border:0.6px solid var(--panel-border);padding:13px 11px 0 11px;color:var(--panel-text)}
  .screen--light .panel{height:507px}
  .screen--dark .panel{height:506px;border:none;padding-top:14px}
  .title{font-size:17.5px;font-weight:600;line-height:18px}
  .page-meta{font-size:5px;font-weight:500;margin-top:2px}
  .rule{height:0.6px;background:var(--rule);margin:8px 0 0}
  .elements-heading{font-size:9px;font-weight:600;margin-top:8px}
  .elements-list{font-size:6.2px;line-height:10.5px;margin-top:4px;white-space:nowrap}

  .sales-table{margin-top:15px;width:607px;background:#fff;border:0.6px solid var(--row-line)}
  .row{display:grid;grid-template-columns:65px 62px 73px 61px 51px 61px 56px 61px 63px 54px;height:18.6px}
  .row + .row{border-top:0.6px solid var(--row-line)}
  .row--head{background:var(--orange);height:20.6px;border-radius:1px 1px 0 0}
  .row--head .cell{color:#fff;font-size:5px;font-weight:500;border:none}
  .cell{display:flex;align-items:center;justify-content:center;font-size:4.3px;color:var(--text-dark);border-left:0.6px solid var(--row-line)}
  .cell:first-child{border-left:none}
  .cell.num{justify-content:flex-start;padding-left:28px}
  .cell.num.same{padding-left:21px}
  .cell.pos{color:var(--green-text)}
  .cell.strong{color:var(--green-text);font-weight:700}
  .cell.ok{background:var(--green-cell)}
  .cell.alert{background:var(--red-cell);color:#fff;font-size:6.6px;padding-left:17px}
</style>
</head>
<body>
<svg width="0" height="0" style="position:absolute" aria-hidden="true">
  <symbol id="i-line" viewBox="0 0 10 10"><path d="M0 0h1.2v8.8H10V10H0z"/><path d="M2 7l2.5-3 2 2L9.5 2l.8.7-3.8 4.8-2-2L2.9 7.7z"/></symbol>
  <symbol id="i-bar" viewBox="0 0 10 10"><path d="M0 0h1.2v8.8H10V10H0z"/><rect x="2.5" y="4" width="1.5" height="4"/><rect x="5" y="2" width="1.5" height="6"/><rect x="7.5" y="5" width="1.5" height="3"/></symbol>
  <symbol id="i-mail" viewBox="0 0 10 10"><path d="M0 2h10v1.2L5 6 0 3.2z"/><path d="M0 4.3l5 2.8 5-2.8V8H0z"/></symbol>
  <symbol id="i-cal" viewBox="0 0 10 10"><path d="M0 2h10v8H0z M1 4v5h8V4z"/><rect x="2" y="0" width="1.2" height="3"/><rect x="6.8" y="0" width="1.2" height="3"/><rect x="2" y="5" width="2" height="1.5"/><rect x="6" y="6.5" width="2" height="1.5"/></symbol>
  <symbol id="i-bell" viewBox="0 0 10 10"><path d="M5 0.5c2 0 3.2 1.5 3.2 3.5v2.5L9.5 8h-9L1.8 6.5V4C1.8 2 3 .5 5 .5z"/><circle cx="5" cy="9" r="1"/></symbol>
  <symbol id="i-menu" viewBox="0 0 10 10"><rect y="1" width="10" height="1.4"/><rect y="4.3" width="10" height="1.4"/><rect y="7.6" width="10" height="1.4"/></symbol>
  <symbol id="i-task" viewBox="0 0 10 10"><path d="M0 0h5l2.5 2.5V5H5v5H0z"/><path d="M6 6h2.5V4.5L10 7 8.5 9.5V8H6z"/></symbol>
  <symbol id="i-news" viewBox="0 0 10 10"><path d="M0 1.5h10v7H0z M1 3v1h8V3z M1 5v1h8V5z M1 7v.6h8V7z" fill-rule="evenodd"/></symbol>
  <symbol id="i-search" viewBox="0 0 10 10"><path d="M4 0a4 4 0 013.2 6.4L10 9.2 9.2 10 6.4 7.2A4 4 0 114 0zm0 1.4a2.6 2.6 0 100 5.2 2.6 2.6 0 000-5.2z"/></symbol>
  <symbol id="i-book" viewBox="0 0 10 10"><path d="M1 8l4-6 5 1-3 5.5z"/><path d="M0 9l1-1 6 .5L6 10z"/></symbol>
  <symbol id="i-gear" viewBox="0 0 10 10"><path d="M4 0h2l.3 1.5 1.3.7L9 1.5l1 1.7-1.1 1v1.6l1.1 1-1 1.7-1.4-.7-1.3.7L6 10H4l-.3-1.5-1.3-.7L1 8.5 0 6.8l1.1-1V4.2L0 3.2 1 1.5l1.4.7 1.3-.7zM5 3.5a1.5 1.5 0 100 3 1.5 1.5 0 000-3z"/></symbol>
</svg>

<div class="canvas">

  <!-- Light theme -->
  <section class="screen screen--light">
    <aside class="sidebar">
      <div class="brand"><span class="brand-mark"></span>Ledgerline</div>
      <ul class="menu">
        <li class="is-active"><svg><use href="#i-line"/></svg><span>Report</span></li>
        <li><svg><use href="#i-bar"/></svg>Charts</li>
        <li><svg><use href="#i-mail"/></svg>Email</li>
        <li><svg><use href="#i-cal"/></svg>Calendar</li>
        <li><svg><use href="#i-bell"/></svg>Notifications</li>
        <li><svg><use href="#i-menu"/></svg>Stand-in</li>
        <li><svg><use href="#i-task"/></svg>Tasks</li>
        <li><svg><use href="#i-line"/></svg>Market</li>
        <li><svg><use href="#i-news"/></svg>News</li>
        <li><svg><use href="#i-search"/></svg>Search</li>
        <li><svg><use href="#i-book"/></svg>Glossary</li>
        <li><svg><use href="#i-gear"/></svg>Setting</li>
      </ul>
    </aside>
    <main class="content">
      <div class="panel">
        <h1 class="title">2021 U.S Sales</h1>
        <p class="page-meta">Page 1 / 107 (2886 records)</p>
        <div class="rule"></div>
        <h2 class="elements-heading">Available Elements:</h2>
        <p class="elements-list">Date, idx_IT Sub Area, Continent, IT Area, Cost element name, Cost Element Group, Cost Element Sub Group, Sum,<br>dup_region, dup_col, date2, name, Sub, Same2, divide, multiply, row_variance, % chng, avg, sqr, root, custom_formula,<br>UK_only, Not_UK, sum, Sum2, div2, row_var2, today, month2, len, rank, left, mid, concat, concat2, style, Month*,</p>
        <div class="sales-table">
          <div class="row row--head"><div class="cell">Styleindex</div><div class="cell">Country</div><div class="cell">Business area</div><div class="cell">Actual</div><div class="cell">Pal</div><div class="cell">Forecast</div><div class="cell">Total</div><div class="cell">Right</div><div class="cell">IT sub Area</div><div class="cell">Same</div></div>
          <div class="row"><div class="cell">Administration</div><div class="cell">Germany</div><div class="cell">Distribution</div><div class="cell num">50598.8</div><div class="cell">0</div><div class="cell num pos">50598.8</div><div class="cell num ok">325177558.9</div><div class="cell">NY</div><div class="cell">Administration</div><div class="cell num same">50708</div></div>
          <div class="row"><div class="cell">Administration</div><div class="cell">Germany</div><div class="cell">Distribution</div><div class="cell num">0</div><div class="cell">0</div><div class="cell num">0</div><div class="cell num">325177558.9</div><div class="cell">NY</div><div class="cell">Administration</div><div class="cell num same">110</div></div>
          <div class="row"><div class="cell">Administration</div><div class="cell">Germany</div><div class="cell">Distribution</div><div class="cell num">0</div><div class="cell">0</div><div class="cell num">0</div><div class="cell num ok">325177558.9</div><div class="cell">NY</div><div class="cell">Administration</div><div class="cell num same">110</div></div>
          <div class="row"><div class="cell">Administration</div><div class="cell">Germany</div><div class="cell">Distribution</div><div class="cell num pos">613.81</div><div class="cell">0</div><div class="cell num pos">613.81</div><div class="cell num ok">325177558.9</div><div class="cell">NY</div><div class="cell">Administration</div><div class="cell num same strong">723</div></div>
          <div class="row"><div class="cell">Administration</div><div class="cell">Germany</div><div class="cell">Distribution</div><div class="cell num pos">11061.1</div><div class="cell">0</div><div class="cell num pos">11061.1</div><div class="cell num ok">325177558.9</div><div class="cell">NY</div><div class="cell">Administration</div><div class="cell num same strong">11171</div></div>
          <div class="row"><div class="cell">Administration</div><div class="cell">Germany</div><div class="cell">Distribution</div><div class="cell num pos">50598.8</div><div class="cell">0</div><div class="cell num pos">50598.8</div><div class="cell num ok">325177558.9</div><div class="cell">NY</div><div class="cell">Administration</div><div class="cell num same strong">13658</div></div>
          <div class="row"><div class="cell">Administration</div><div class="cell">Germany</div><div class="cell">Distribution</div><div class="cell num pos">024442.02</div><div class="cell">0</div><div class="cell num">0</div><div class="cell num ok">325177558.9</div><div class="cell">NY</div><div class="cell">Administration</div><div class="cell num same strong">18088</div></div>
          <div class="row"><div class="cell">Administration</div><div class="cell">Germany</div><div class="cell">Distribution</div><div class="cell num pos">24442</div><div class="cell">0</div><div class="cell num">0</div><div class="cell num">325177558.9</div><div class="cell">NY</div><div class="cell">Administration</div><div class="cell num same strong">2665</div></div>
          <div class="row"><div class="cell">Administration</div><div class="cell">Germany</div><div class="cell">Distribution</div><div class="cell num pos">613.81</div><div class="cell">0</div><div class="cell num">613.81</div><div class="cell num ok">325177558.9</div><div class="cell">NY</div><div class="cell">Administration</div><div class="cell num same">2122</div></div>
          <div class="row"><div class="cell">Administration</div><div class="cell">Germany</div><div class="cell">Distribution</div><div class="cell num pos">11061.1</div><div class="cell">0</div><div class="cell num">11061.1</div><div class="cell num">325177558.9</div><div class="cell">NY</div><div class="cell">Administration</div><div class="cell num same">3020</div></div>
          <div class="row"><div class="cell">Administration</div><div class="cell">Germany</div><div class="cell">Distribution</div><div class="cell num pos">50598.8</div><div class="cell">0</div><div class="cell num">50598.8</div><div class="cell num ok">325177558.9</div><div class="cell">NY</div><div class="cell">Administration</div><div class="cell num same">68603</div></div>
          <div class="row"><div class="cell">Administration</div><div class="cell">Germany</div><div class="cell">Distribution</div><div class="cell num">0</div><div class="cell">0</div><div class="cell num">0</div><div class="cell num">325177558.9</div><div class="cell">NY</div><div class="cell">Administration</div><div class="cell num same">765</div></div>
          <div class="row"><div class="cell">Administration</div><div class="cell">Germany</div><div class="cell">Distribution</div><div class="cell num">0</div><div class="cell">0</div><div class="cell num">0</div><div class="cell num">325177558.9</div><div class="cell">NY</div><div class="cell">Administration</div><div class="cell num same">110</div></div>
          <div class="row"><div class="cell">Administration</div><div class="cell">Germany</div><div class="cell">Distribution</div><div class="cell num">613.81</div><div class="cell">0</div><div class="cell num pos">613.81</div><div class="cell num alert">-6144.57</div><div class="cell">NY</div><div class="cell">Administration</div><div class="cell num same alert">-55815</div></div>
          <div class="row"><div class="cell">Administration</div><div class="cell">Germany</div><div class="cell">Distribution</div><div class="cell num">11061.1</div><div class="cell">0</div><div class="cell num pos">11061.1</div><div class="cell num">325177558.9</div><div class="cell">NY</div><div class="cell">Administration</div><div class="cell num same alert">-10540</div></div>
          <div class="row"><div class="cell">Administration</div><div class="cell">Germany</div><div class="cell">Distribution</div><div class="cell num">50598.8</div><div class="cell">0</div><div class="cell num pos">50598.8</div><div class="cell num">325177558.9</div><div class="cell">NY</div><div class="cell">Administration</div><div class="cell num same">110</div></div>
          <div class="row"><div class="cell">Administration</div><div class="cell">Germany</div><div class="cell">Distribution</div><div class="cell num">0</div><div class="cell">0</div><div class="cell num">0</div><div class="cell num">325177558.9</div><div class="cell">NY</div><div class="cell">Administration</div><div class="cell num same alert">-8428</div></div>
          <div class="row"><div class="cell">Administration</div><div class="cell">Germany</div><div class="cell">Distribution</div><div class="cell num">0</div><div class="cell">0</div><div class="cell num">0</div><div class="cell num">325177558.9</div><div class="cell">NY</div><div class="cell">Administration</div><div class="cell num same">110</div></div>
          <div class="row"><div class="cell">Administration</div><div class="cell">Germany</div><div class="cell">Distribution</div><div class="cell num">613.81</div><div class="cell">0</div><div class="cell num">613.81</div><div class="cell num">325177558.9</div><div class="cell">NY</div><div class="cell">Administration</div><div class="cell num same">1183</div></div>
        </div>
      </div>
    </main>
  </section>

  <!-- Dark theme -->
  <section class="screen screen--dark">
    <aside class="sidebar">
      <div class="brand"><span class="brand-mark"></span>Ledgerline</div>
      <ul class="menu">
        <li class="is-active"><svg><use href="#i-line"/></svg><span>Report</span></li>
        <li><svg><use href="#i-bar"/></svg>Charts</li>
        <li><svg><use href="#i-mail"/></svg>Email</li>
        <li><svg><use href="#i-cal"/></svg>Calendar</li>
        <li><svg><use href="#i-bell"/></svg>Notifications</li>
        <li><svg><use href="#i-menu"/></svg>Stand-in</li>
        <li><svg><use href="#i-task"/></svg>Tasks</li>
        <li><svg><use href="#i-line"/></svg>Market</li>
        <li><svg><use href="#i-news"/></svg>News</li>
        <li><svg><use href="#i-search"/></svg>Search</li>
        <li><svg><use href="#i-book"/></svg>Glossary</li>
        <li><svg><use href="#i-gear"/></svg>Setting</li>
      </ul>
    </aside>
    <main class="content">
      <div class="panel">
        <h1 class="title">2021 U.S Sales</h1>
        <p class="page-meta">Page 1 / 107 (2886 records)</p>
        <div class="rule"></div>
        <h2 class="elements-heading">Available Elements:</h2>
        <p class="elements-list">Date, idx_IT Sub Area, Continent, IT Area, Cost element name, Cost Element Group, Cost Element Sub Group, Sum,<br>dup_region, dup_col, date2, name, Sub, Same2, divide, multiply, row_variance, % chng, avg, sqr, root, custom_formula,<br>UK_only, Not_UK, sum, Sum2, div2, row_var2, today, month2, len, rank, left, mid, concat, concat2, style, Month*,</p>
        <div class="sales-table">
          <div class="row row--head"><div class="cell">Styleindex</div><div class="cell">Country</div><div class="cell">Business area</div><div class="cell">Actual</div><div class="cell">Pal</div><div class="cell">Forecast</div><div class="cell">Total</div><div class="cell">Right</div><div class="cell">IT sub Area</div><div class="cell">Same</div></div>
          <div class="row"><div class="cell">Administration</div><div class="cell">Germany</div><div class="cell">Distribution</div><div class="cell num">50598.8</div><div class="cell">0</div><div class="cell num pos">50598.8</div><div class="cell num ok">325177558.9</div><div class="cell">NY</div><div class="cell">Administration</div><div class="cell num same">50708</div></div>
          <div class="row"><div class="cell">Administration</div><div class="cell">Germany</div><div class="cell">Distribution</div><div class="cell num">0</div><div class="cell">0</div><div class="cell num">0</div><div class="cell num">325177558.9</div><div class="cell">NY</div><div class="cell">Administration</div><div class="cell num same">110</div></div>
          <div class="row"><div class="cell">Administration</div><div class="cell">Germany</div><div class="cell">Distribution</div><div class="cell num">0</div><div class="cell">0</div><div class="cell num">0</div><div class="cell num ok">325177558.9</div><div class="cell">NY</div><div class="cell">Administration</div><div class="cell num same">110</div></div>
          <div class="row"><div class="cell">Administration</div><div class="cell">Germany</div><div class="cell">Distribution</div><div class="cell num pos">613.81</div><div class="cell">0</div><div class="cell num pos">613.81</div><div class="cell num ok">325177558.9</div><div class="cell">NY</div><div class="cell">Administration</div><div class="cell num same strong">723</div></div>
          <div class="row"><div class="cell">Administration</div><div class="cell">Germany</div><div class="cell">Distribution</div><div class="cell num pos">11061.1</div><div class="cell">0</div><div class="cell num pos">11061.1</div><div class="cell num ok">325177558.9</div><div class="cell">NY</div><div class="cell">Administration</div><div class="cell num same strong">11171</div></div>
          <div class="row"><div class="cell">Administration</div><div class="cell">Germany</div><div class="cell">Distribution</div><div class="cell num pos">50598.8</div><div class="cell">0</div><div class="cell num pos">50598.8</div><div class="cell num ok">325177558.9</div><div class="cell">NY</div><div class="cell">Administration</div><div class="cell num same strong">13658</div></div>
          <div class="row"><div class="cell">Administration</div><div class="cell">Germany</div><div class="cell">Distribution</div><div class="cell num pos">024442.02</div><div class="cell">0</div><div class="cell num">0</div><div class="cell num ok">325177558.9</div><div class="cell">NY</div><div class="cell">Administration</div><div class="cell num same strong">18088</div></div>
          <div class="row"><div class="cell">Administration</div><div class="cell">Germany</div><div class="cell">Distribution</div><div class="cell num pos">24442</div><div class="cell">0</div><div class="cell num">0</div><div class="cell num">325177558.9</div><div class="cell">NY</div><div class="cell">Administration</div><div class="cell num same strong">2665</div></div>
          <div class="row"><div class="cell">Administration</div><div class="cell">Germany</div><div class="cell">Distribution</div><div class="cell num pos">613.81</div><div class="cell">0</div><div class="cell num">613.81</div><div class="cell num ok">325177558.9</div><div class="cell">NY</div><div class="cell">Administration</div><div class="cell num same">2122</div></div>
          <div class="row"><div class="cell">Administration</div><div class="cell">Germany</div><div class="cell">Distribution</div><div class="cell num pos">11061.1</div><div class="cell">0</div><div class="cell num">11061.1</div><div class="cell num">325177558.9</div><div class="cell">NY</div><div class="cell">Administration</div><div class="cell num same">3020</div></div>
          <div class="row"><div class="cell">Administration</div><div class="cell">Germany</div><div class="cell">Distribution</div><div class="cell num pos">50598.8</div><div class="cell">0</div><div class="cell num">50598.8</div><div class="cell num ok">325177558.9</div><div class="cell">NY</div><div class="cell">Administration</div><div class="cell num same">68603</div></div>
          <div class="row"><div class="cell">Administration</div><div class="cell">Germany</div><div class="cell">Distribution</div><div class="cell num">0</div><div class="cell">0</div><div class="cell num">0</div><div class="cell num">325177558.9</div><div class="cell">NY</div><div class="cell">Administration</div><div class="cell num same">765</div></div>
          <div class="row"><div class="cell">Administration</div><div class="cell">Germany</div><div class="cell">Distribution</div><div class="cell num">0</div><div class="cell">0</div><div class="cell num">0</div><div class="cell num">325177558.9</div><div class="cell">NY</div><div class="cell">Administration</div><div class="cell num same">110</div></div>
          <div class="row"><div class="cell">Administration</div><div class="cell">Germany</div><div class="cell">Distribution</div><div class="cell num">613.81</div><div class="cell">0</div><div class="cell num pos">613.81</div><div class="cell num alert">-6144.57</div><div class="cell">NY</div><div class="cell">Administration</div><div class="cell num same alert">-55815</div></div>
          <div class="row"><div class="cell">Administration</div><div class="cell">Germany</div><div class="cell">Distribution</div><div class="cell num">11061.1</div><div class="cell">0</div><div class="cell num pos">11061.1</div><div class="cell num">325177558.9</div><div class="cell">NY</div><div class="cell">Administration</div><div class="cell num same alert">-10540</div></div>
          <div class="row"><div class="cell">Administration</div><div class="cell">Germany</div><div class="cell">Distribution</div><div class="cell num">50598.8</div><div class="cell">0</div><div class="cell num pos">50598.8</div><div class="cell num">325177558.9</div><div class="cell">NY</div><div class="cell">Administration</div><div class="cell num same">110</div></div>
          <div class="row"><div class="cell">Administration</div><div class="cell">Germany</div><div class="cell">Distribution</div><div class="cell num">0</div><div class="cell">0</div><div class="cell num">0</div><div class="cell num">325177558.9</div><div class="cell">NY</div><div class="cell">Administration</div><div class="cell num same alert">-8428</div></div>
          <div class="row"><div class="cell">Administration</div><div class="cell">Germany</div><div class="cell">Distribution</div><div class="cell num">0</div><div class="cell">0</div><div class="cell num">0</div><div class="cell num">325177558.9</div><div class="cell">NY</div><div class="cell">Administration</div><div class="cell num same">110</div></div>
          <div class="row"><div class="cell">Administration</div><div class="cell">Germany</div><div class="cell">Distribution</div><div class="cell num">613.81</div><div class="cell">0</div><div class="cell num">613.81</div><div class="cell num">325177558.9</div><div class="cell">NY</div><div class="cell">Administration</div><div class="cell num same">1183</div></div>
        </div>
      </div>
    </main>
  </section>

</div>
</body>
</html>
```